Educational non-profit needs an End of the Year Flyer

We need a flyer to mail to our supporters asking for donations to our program. Hillcrest Open Learning Hub runs after school programs for low-income students in Pasadena, CA. This is our end of the year mailing to supporters asking them to finish out the year with their contributions so that we can meet our budget.

Target Market(s)

Donors and supporters of organization

Industry/Entity Type

Non-Profit

Font styles to use
Serif

Colors

Designer to choose colors to be used in the design.

Requirements
Must have
• The project should fit on a 6x9" card, and be printed on front and back. It should show pictures, use the copy I have included, a space for a label address, a stamp, and the return address.
Nice to have
• eye-catching, fun

```html
<!DOCTYPE html>
<html lang="en">
<head>
<meta charset="utf-8">
<title>Hillcrest Open Learning Hub – End of Year Postcard</title>
<link rel="stylesheet" href="https://fonts.googleapis.com/css2?family=Fredoka:wght@600;700&family=Montserrat:wght@400;500;600&display=swap">
<style>
  :root{
    --bg:#e4e6e7;
    --paper:#ffffff;
    --ink:#1f1f1f;
    --bar:#262626;
    --yellow:#fff200;
    --muted:#d8d8d8;
    --line:#bdbdbd;
  }
  *{box-sizing:border-box;margin:0;padding:0}
  html,body{width:1200px;height:1200px;overflow:hidden;background:var(--bg);font-family:"Montserrat",sans-serif;color:var(--ink)}
  .card{position:absolute;width:780px;height:520px;background:var(--paper);box-shadow:0 6px 18px rgba(0,0,0,.18);overflow:hidden}
  .card--front{left:60px;top:40px}
  .card--back{left:360px;top:640px}
  .abs{position:absolute}
  .photo{position:absolute}

  /* front */
  .brand-mark{left:20px;top:34px;width:130px;display:flex;flex-direction:column;align-items:center;gap:8px}
  .brand-mark__dot{width:66px;height:66px;border-radius:50%;background:var(--yellow);border:3px solid var(--ink)}
  .brand-mark__name{font-family:"Fredoka",sans-serif;font-weight:600;font-size:13px;text-align:center;line-height:1.2}
  .title{left:170px;top:20px;font-family:"Fredoka",sans-serif;font-weight:700;font-size:46px;line-height:1;letter-spacing:.3px}
  .tagline{left:172px;top:118px;font-size:14px;font-weight:500;width:290px;line-height:1.3}
  .photo--writing{left:0;top:250px;width:200px;height:190px;background:linear-gradient(160deg,#c9b37a,#8a6f4a)}
  .photo--swing{left:200px;top:180px;width:290px;height:190px;background:linear-gradient(150deg,#b5b5b5,#7d7d7d)}
  .photo--sisters{left:490px;top:120px;width:290px;height:260px;background:linear-gradient(160deg,#2a2216,#7a4a32 60%,#c58a5e)}
  .appeal{left:200px;top:370px;width:400px;height:70px;background:var(--yellow);padding:10px 18px;font-weight:600;font-size:20px;line-height:1.2;text-transform:uppercase}
  .social-strip{left:600px;top:380px;width:180px;height:60px;background:var(--bar);color:#fff;font-size:11px;display:flex;align-items:center;gap:8px;padding:0 12px}
  .footer{display:flex;align-items:center;gap:34px;background:var(--bar);color:#fff;font-size:12px;padding:0 24px}
  .footer--front{left:0;top:440px;width:780px;height:80px}
  .contact{display:flex;align-items:center;gap:7px}
  .contact svg{width:14px;height:14px;flex:none}
  .social-dot{width:12px;height:12px;border-radius:50%;border:1.5px solid #fff;flex:none}

  /* back */
  .photo--guitars{left:0;top:40px;width:470px;height:150px;background:linear-gradient(160deg,#4a3328,#9a6e52 55%,#d8b08a)}
  .photo--park{left:260px;top:190px;width:210px;height:100px;background:linear-gradient(160deg,#8aa26a,#c8b08a)}
  .photo--group{left:260px;top:290px;width:210px;height:120px;background:linear-gradient(160deg,#6a4a3a,#a88262)}
  .letter{left:20px;top:204px;width:228px;font-size:10.5px;line-height:1.45;text-align:justify}
  .giving{left:0;top:410px;width:470px;height:62px;background:var(--yellow);padding:8px 20px}
  .giving__note{font-size:10px;font-weight:600;text-transform:uppercase;letter-spacing:.3px}
  .giving__greeting{font-weight:600;font-size:19px;line-height:1.2;margin-top:3px}
  .footer--back{left:0;top:472px;width:470px;height:48px;gap:22px;padding:0 20px;font-size:10.5px}
  .return-address{left:500px;top:28px;font-size:11.5px;line-height:1.45;width:170px;font-style:normal}
  .stamp{left:682px;top:20px;width:76px;height:86px;background:var(--muted)}
  .address-lines{left:520px;top:250px;width:238px;display:flex;flex-direction:column;gap:30px}
  .address-lines span{display:block;height:1px;background:var(--line)}
</style>
</head>
<body>

<section class="card card--front" aria-label="Postcard front">
  <div class="abs brand-mark">
    <span class="brand-mark__dot"></span>
    <span class="brand-mark__name">Hillcrest Open Learning Hub</span>
  </div>
  <h1 class="abs title">Hillcrest Open<br>Learning Hub</h1>
  <p class="abs tagline">Educational and community-building programs for children, youth and families</p>

  <div class="photo photo--writing" role="img" aria-label="Photo of a smiling girl in a classroom holding up a handwritten letter"></div>
  <div class="photo photo--swing" role="img" aria-label="Black and white photo of a young girl on a tire swing"></div>
  <div class="photo photo--sisters" role="img" aria-label="Photo of two sisters hugging outdoors at night"></div>

  <div class="abs appeal">We need your help to<br>finish out 2018 strong!</div>
  <div class="abs social-strip"><span class="social-dot"></span>Hillcrest Open Learning Hub</div>

  <div class="abs footer footer--front">
    <span class="contact">
      <svg viewBox="0 0 16 16"><path fill="#fff" d="M4 1l3 3-2 2c1 2 3 4 5 5l2-2 3 3-2 3C7 15 1 9 1 3z"/></svg>(626) 555-0147
    </span>
    <span class="contact">
      <svg viewBox="0 0 16 16"><circle cx="8" cy="8" r="6.5" fill="none" stroke="#fff" stroke-width="1.5"/><path d="M1.5 8h13M8 1.5c-3 3.5-3 9.5 0 13M8 1.5c3 3.5 3 9.5 0 13" fill="none" stroke="#fff" stroke-width="1.2"/></svg>www.hillcrest-learns.org
    </span>
    <span class="contact">
      <svg viewBox="0 0 16 16"><rect x="1.5" y="3.5" width="13" height="9" fill="none" stroke="#fff" stroke-width="1.5"/><path d="M1.5 3.5l6.5 5 6.5-5" fill="none" stroke="#fff" stroke-width="1.5"/></svg>hello@hillcrest-learns.org
    </span>
  </div>
</section>

<section class="card card--back" aria-label="Postcard back">
  <div class="photo photo--guitars" role="img" aria-label="Photo of students playing guitars in an after school music class"></div>
  <div class="photo photo--park" role="img" aria-label="Photo of children gathered on a park bench"></div>
  <div class="photo photo--group" role="img" aria-label="Group photo of students and staff in a hallway"></div>

  <p class="abs letter">We have had a wonderful 25th year of serving the children and families of Pasadena here at Hillcrest Open Learning Hub with high quality afterschool programs. Hundreds and hundreds of students have been a part of the Hillcrest Kids Club family. Our annual budget is $275,000 and we count on $100,000 from individual donors. Will you join with us for an end of the year contribution?</p>

  <div class="abs giving">
    <p class="giving__note">Remember, you can give online through GivePort.</p>
    <p class="giving__greeting">Merry Christmas from all of us at HOLH!</p>
  </div>

  <div class="abs footer footer--back">
    <span class="contact">
      <svg viewBox="0 0 16 16"><path fill="#fff" d="M4 1l3 3-2 2c1 2 3 4 5 5l2-2 3 3-2 3C7 15 1 9 1 3z"/></svg>(626) 555-0147
    </span>
    <span class="contact"><span class="social-dot"></span>Hillcrest Open Learning Hub</span>
  </div>

  <address class="abs return-address">
    Hillcrest Open Learning Hub<br>
    214 N. Alder Ave.<br>
    Pasadena, CA 91106<br>
    (626) 555-0147
  </address>
  <div class="abs stamp" aria-label="Stamp area"></div>
  <div class="abs address-lines" aria-label="Mailing address area">
    <span></span><span></span><span></span><span></span>
  </div>
</section>

</body>
</html>
```